Design a Bold Tradeshow Backdrop for a Sustainable Cleaning Technology

We need a professional, high-impact 10' × 8' tradeshow backdrop for Vornelle®, a commercial cleaning technology company. 143.75" x 90" high and needs bleeds in the 143.75" direction for printing but the graphic area is 10' wide.

Our first event will have an audience that includes K–12 school administrators, facility managers, business officials, and custodial decision-makers. However, this backdrop will be used at multiple future trade shows across different commercial and institutional markets.

The design therefore needs to be universal rather than specifically education- or school-themed.

Our goal is to stop attendees as they walk past the booth and immediately communicate a simple message:

Safer and more sustainable cleaning can also cost substantially less than conventional cleaning chemicals.

We want the design to feel modern, innovative, clean, sustainable, credible, commercial, and premium. It should resonate with K–12 decision-makers while being equally appropriate at events serving commercial facilities, healthcare, hospitality, government, property management, transportation, and other institutional markets.

It should NOT look like a traditional janitorial supply advertisement and should not be overly busy.

The most important messages need to be understandable from approximately 10–20 feet away.

Required Messaging

The primary headline should be:

SUSTAINABLE CLEANING
DOES NOT HAVE TO BE EXPENSIVE.

Three major value propositions should be prominently displayed:

FREE
Cleaning Chemical Analysis
See how much you can save.

SAVE UP TO 60% or More
on Cleaning Chemical Costs

AS LITTLE AS $0.27/GALLON

We would also like a strong secondary message incorporated into the design:

SMARTER CLEANING.
High Performance. Low Cost. Safer.

Visual Direction — Important

Rather than showing a K–12 school hallway or other environment that limits the backdrop to the education market, we want a sophisticated, universal commercial or institutional environment.

This could be a bright, contemporary commercial facility, lobby, corridor, office environment, public building, or other premium architectural space that could reasonably represent many different types of facilities.

The environment should communicate:

Cleanliness • Safety • Sustainability • Professionalism • Efficiency • High Performance

We want someone from a school, hospital, hotel, office building, airport, government facility, or other commercial property to be able to look at the backdrop and relate the imagery to their own facility.

Please avoid imagery that makes the backdrop industry-specific.

We also want to avoid clichéd environmental imagery. The design does not need to be covered in leaves, trees, water droplets, recycling symbols, or other obvious "green" graphics to communicate sustainability. We prefer a sophisticated commercial interpretation of sustainability.

Color & Brand Direction

We want the overall color palette to stay primarily within:

Blues — consistent with our corporate identity

Greens — to reinforce sustainability, safety, efficiency, and environmental responsibility

White — strongly encouraged for clean space, contrast, and an open contemporary appearance

Black — should be limited primarily to text where necessary for readability

Please avoid making black a major background or dominant design color.

We want the finished display to have a bright, clean, sophisticated, sustainable look and feel rather than a dark or industrial appearance.

The design should use significant negative space and a strong visual hierarchy.

Less is more.

We prefer a few large, powerful messages that can be understood quickly rather than numerous small bullet points, paragraphs, or icons.

Creative Freedom

The attached concept image is provided to communicate our general direction and messaging only.

It does not need to be copied.

We are specifically running this contest because we want designers to improve upon our initial concept and show us different creative approaches to presenting the Vornelle value proposition.

We are open to creative interpretations of the commercial environment, composition, typography, use of negative space, and how the three major financial benefits are presented.

The finished design should feel like an innovative commercial technology brand, not simply another cleaning chemical company.

Corporate Logo — Very Important

We are attaching our official Vornelle® corporate logo for use in the design.

DO NOT redraw, recreate, modify, stylize, reinterpret, trace, or AI-generate the Vornelle logo.

The supplied corporate logo must be inserted directly into the artwork exactly as provided, maintaining its original proportions, colors, typography, trademark elements, and graphic design.

The logo should generally appear in the upper-left area of the backdrop but should not overwhelm the primary marketing message.

Printer Template & Graphic Sizing

We are also attaching the printer's official graphic template and instructions for the 8' × 8' tension-fabric display.

Designers should create their artwork using these supplied specifications so the winning design can be transferred directly into production.

The printer requires that the original document size not be changed, artwork be created on the designated design layer or a new layer, images be embedded, text be converted to outlines, and the finished production artwork be supplied as a PDF.

Please pay particular attention to the bleed area, finished size, and safe artwork area when positioning important text, graphics, and the corporate logo.

Physical Booth Context

The backdrop will sit behind an 8' tradeshow table.

The complete booth will also contain:

A blue stretch tablecloth with the Vornelle corporate logo
BrevoMax and Vornelle product containers and samples on the table
An HulaDrent chemical mixing/dilution station displayed on an elevated stand to the left
A television/monitor to the right demonstrating our online ROI cost-savings calculator

Because these other booth elements will explain our products and technology in greater detail, the backdrop should NOT attempt to explain everything we do.

Its primary purpose is to stop traffic, establish the Vornelle brand, and communicate our core economic and sustainability value proposition.

Final Deliverables

The winning designer must provide artwork properly sized and positioned using our supplied 8' × 8' tension-fabric display template.

Final files should include:

Print-ready, high-resolution PDF
Editable source/vector artwork
All images embedded
Fonts converted to outlines
Artwork correctly positioned within the supplied printer template
Original Vornelle corporate logo incorporated without modification
The 3–5 Second Test

This is perhaps the most important requirement.

Someone walking down a tradeshow aisle should be able to look at the backdrop for 3–5 seconds and understand:

Vornelle offers safer, sustainable, high-performance commercial cleaning — at a lower cost.

The three offers we particularly want them to remember are:

FREE CHEMICAL ANALYSIS

SAVE UP TO 60%

AS LITTLE AS $0.27/GALLON

The overall takeaway should be:

Sustainable cleaning does not have to cost more.

We want the winning design to make that message immediately understandable, credible, and memorable.

Colors
0054AA
0677BA
7BADD7
CADEEF
E8F1F8
0094D4
00A9DD
6FCCEA
C7EBF8
E9F6FB
00AB8E
00BBA5
67D7C9
C6EFE9
E9F9F6
59FF00
82FF00
B8FF75
E3FFCB
F4FFEA

```html
<!DOCTYPE html>
<html lang="en">
<head>
<meta charset="UTF-8">
<title>Vornelle – Sustainable Cleaning Backdrop</title>
<link rel="stylesheet" href="https://fonts.googleapis.com/css2?family=Archivo:ital,wdth,wght@0,62..125,100..900;1,62..125,100..900&family=Poppins:ital,wght@0,400;0,500;0,600;1,400;1,500&display=swap">
<style>
  :root {
    --brand-blue: #0054AA;
    --mid-blue: #0677BA;
    --sky: #00A9DD;
    --teal: #00AB8E;
    --teal-soft: #67D7C9;
    --white: #ffffff;
    --ink: #111111;
    --accent-green: #2fd39a;
  }
  * { margin: 0; padding: 0; box-sizing: border-box; }
  html, body { width: 1200px; height: 1200px; overflow: hidden; background: var(--white); }
  .backdrop {
    position: relative; width: 1200px; height: 1200px; overflow: hidden;
    font-family: "Poppins", sans-serif; color: var(--ink);
    background: linear-gradient(120deg, #ffffff 0%, #f7fafc 45%, #eef4f8 70%, #e6eef4 100%);
  }
  .abs { position: absolute; }
  .lobby-photo {
    position: absolute; left: 560px; top: 0; width: 640px; height: 900px;
    background: radial-gradient(ellipse at 60% 40%, #f4f8fb 0%, #e3ecf2 55%, #d7e4ec 100%);
    opacity: .85;
  }
  .machine-photo {
    position: absolute; left: 641px; top: 349px; width: 477px; height: 461px;
    border-radius: 24px;
    background: linear-gradient(160deg, #5b8fc7 0%, #6aa9cf 40%, #9fbccd 75%, #c9d6de 100%);
    opacity: .75;
  }
  .waves { position: absolute; left: 0; top: 0; }

  .brand-name { left: 44px; top: 58px; font-family: "Archivo", sans-serif; font-weight: 800; font-size: 62px; color: var(--ink); letter-spacing: -1px; line-height: 1; }
  .brand-tag { left: 44px; top: 150px; font-size: 17px; letter-spacing: 2.6px; color: var(--ink); font-weight: 500; }

  .hl { position: absolute; left: 44px; font-family: "Archivo", sans-serif; font-weight: 800; line-height: 1; white-space: nowrap; margin: 0; }
  .hl-sustainable { top: 219px; font-size: 75px; color: var(--brand-blue); font-stretch: 87%; }
  .hl-cleaning { top: 285px; font-size: 100px; color: var(--teal); font-stretch: 95%; letter-spacing: -1px; }
  .hl-does { top: 379px; font-size: 50px; color: var(--brand-blue); font-stretch: 85%; }
  .hl-expensive { top: 424px; font-size: 72px; color: var(--brand-blue); font-stretch: 88%; }
  .rule { left: 48px; top: 522px; width: 478px; height: 5px;
    background: linear-gradient(90deg, var(--teal) 0%, var(--teal-soft) 60%, rgba(103,215,201,0) 100%); }

  .offer { position: absolute; top: 560px; width: 210px; text-align: center; }
  .offer-icon { display: block; margin: 0 auto; }
  .offer-big { font-family: "Archivo", sans-serif; font-weight: 900; line-height: 1; }
  .offer-free { left: 17px; }
  .offer-free .offer-big { font-size: 64px; color: var(--brand-blue); margin-top: 8px; }
  .offer-save { left: 230px; }
  .offer-save .offer-big { font-size: 64px; color: var(--teal); margin-top: 8px; }
  .offer-price { left: 449px; width: 220px; }
  .small-dark { font-size: 15px; line-height: 18px; font-weight: 500; color: var(--ink); }
  .small-note { font-size: 15px; line-height: 18px; font-style: italic; color: var(--brand-blue); }
  .upto { font-family: "Archivo", sans-serif; font-weight: 900; color: var(--teal); font-size: 24px; line-height: 1.1; margin-top: 2px; }
  .upto b { font-size: 34px; }
  .as-little { font-family: "Archivo", sans-serif; font-weight: 800; color: var(--brand-blue); font-size: 24px; margin-top: 6px; line-height: 1; }
  .price { font-family: "Archivo", sans-serif; font-weight: 900; color: var(--brand-blue); font-size: 70px; line-height: 1; letter-spacing: -1px; }
  .per-gallon { font-weight: 600; font-size: 24px; color: var(--ink); line-height: 1.1; }
  .divider { position: absolute; top: 589px; width: 2px; height: 212px; background: var(--teal); }

  .smarter { left: 845px; top: 108px; font-family: "Archivo", sans-serif; font-style: italic; font-weight: 900; line-height: 48px; font-size: 52px; }
  .smarter .l1 { color: var(--brand-blue); display: block; }
  .smarter .l2 { color: var(--teal); display: block; }
  .smarter-rule { left: 847px; top: 218px; width: 88px; height: 4px; background: var(--teal); }
  .benefits { left: 848px; top: 243px; font-size: 22px; font-weight: 600; line-height: 29px; color: var(--ink); }

  .pillar { position: absolute; top: 1030px; width: 180px; text-align: center; color: var(--white); font-size: 16px; line-height: 21px; text-transform: uppercase; }
  .pillar svg { display: block; margin: 0 auto 10px; }
  .pillar-divider { position: absolute; top: 1035px; width: 1.5px; height: 98px; background: rgba(255,255,255,.75); }
  .closing { left: 845px; top: 1062px; font-size: 19px; line-height: 25px; color: var(--white); }
  .closing .accent { color: var(--accent-green); }
</style>
</head>
<body>
<div class="backdrop">
  <div class="lobby-photo" role="img" aria-label="Bright modern commercial lobby with curved white balconies and glass walls"></div>
  <div class="machine-photo" role="img" aria-label="Custodian driving a blue ride-on floor scrubber across a polished floor"></div>

  <svg class="waves" width="1200" height="1200" viewBox="0 0 1200 1200" aria-hidden="true">
    <defs>
      <linearGradient id="blueBand" x1="0" y1="0" x2="1" y2="1">
        <stop offset="0" stop-color="#0a55b5"/>
        <stop offset="1" stop-color="#1747a6"/>
      </linearGradient>
      <linearGradient id="tealBand" x1="0" y1="1" x2="1" y2="0">
        <stop offset="0" stop-color="#00AB8E"/>
        <stop offset="1" stop-color="#0fb596"/>
      </linearGradient>
    </defs>
    <path d="M0 778 C120 870 260 940 380 995 L0 995 Z" fill="#4dc6ea"/>
    <path d="M0 826 C200 955 480 1000 760 992 C950 986 1100 945 1200 880 V1200 H0 Z" fill="url(#blueBand)"/>
    <path d="M430 992 C760 988 1050 900 1200 678 V862 C1060 950 800 990 430 992 Z" fill="url(#tealBand)"/>
    <path d="M440 998 C780 996 1060 930 1200 866" fill="none" stroke="#ffffff" stroke-width="3" opacity=".85"/>
  </svg>

  <div class="abs brand-name">Vornelle®</div>
  <div class="abs brand-tag">CLEARGUARD™</div>

  <h1 class="headline">
    <span class="hl hl-sustainable">SUSTAINABLE</span>
    <span class="hl hl-cleaning">CLEANING</span>
    <span class="hl hl-does">DOES NOT HAVE TO</span>
    <span class="hl hl-expensive">BE EXPENSIVE.</span>
  </h1>
  <div class="abs rule"></div>

  <div class="offer offer-free">
    <svg class="offer-icon" width="84" height="84" viewBox="0 0 84 84" aria-hidden="true">
      <circle cx="42" cy="42" r="41" fill="#0054AA"/>
      <path d="M34 20 H50 M37 20 V38 L25 60 Q23 64 28 64 H56 Q61 64 59 60 L47 38 V20" fill="none" stroke="#fff" stroke-width="4" stroke-linejoin="round"/>
      <path d="M30 52 H54 L58 61 H26 Z" fill="#fff"/>
      <circle cx="40" cy="46" r="2.5" fill="#fff"/><circle cx="46" cy="43" r="2" fill="#fff"/>
    </svg>
    <div class="offer-big">FREE</div>
    <div class="small-dark">Cleaning<br>Chemical Analysis</div>
    <div class="small-note">See how much<br>you can save.</div>
  </div>
  <div class="divider" style="left:229px"></div>

  <div class="offer offer-save">
    <svg class="offer-icon" width="84" height="84" viewBox="0 0 84 84" aria-hidden="true">
      <circle cx="42" cy="42" r="41" fill="#00AB8E"/>
      <rect x="24" y="48" width="6" height="14" fill="#fff"/>
      <rect x="33" y="42" width="6" height="20" fill="#fff"/>
      <rect x="42" y="46" width="6" height="16" fill="#fff"/>
      <rect x="51" y="38" width="6" height="24" fill="#fff"/>
      <path d="M22 40 L34 30 L44 36 L58 22" fill="none" stroke="#fff" stroke-width="4"/>
      <path d="M50 21 H59 V30" fill="none" stroke="#fff" stroke-width="4"/>
    </svg>
    <div class="offer-big">SAVE</div>
    <div class="upto">UP TO <b>60%</b></div>
    <div class="small-dark">on Cleaning<br>Chemical Costs</div>
  </div>
  <div class="divider" style="left:444px"></div>

  <div class="offer offer-price">
    <svg class="offer-icon" width="84" height="84" viewBox="0 0 84 84" aria-hidden="true">
      <circle cx="42" cy="42" r="41" fill="#0054AA"/>
      <text x="42" y="58" text-anchor="middle" font-family="Archivo, sans-serif" font-weight="900" font-size="46" fill="#fff">$</text>
    </svg>
    <div class="as-little">AS LITTLE AS</div>
    <div class="price">$0.27</div>
    <div class="per-gallon">/GALLON</div>
  </div>

  <div class="abs smarter"><span class="l1">SMARTER</span><span class="l2">CLEANING.</span></div>
  <div class="abs smarter-rule"></div>
  <div class="abs benefits">High Performance.<br>Low Cost.<br>Safer.</div>

  <div class="pillar" style="left:33px">
    <svg width="50" height="54" viewBox="0 0 50 54" aria-hidden="true">
      <path d="M25 2 L46 10 V26 C46 40 36 48 25 52 C14 48 4 40 4 26 V10 Z" fill="none" stroke="#fff" stroke-width="2"/>
      <path d="M15 27 L22 34 L36 20" fill="none" stroke="#fff" stroke-width="2.5"/>
    </svg>
    Safer for people<br>and facilities
  </div>
  <div class="pillar-divider" style="left:220px"></div>
  <div class="pillar" style="left:215px">
    <svg width="50" height="54" viewBox="0 0 50 54" aria-hidden="true">
      <path d="M8 46 C6 24 22 8 46 6 C46 30 32 46 8 46 Z" fill="none" stroke="#fff" stroke-width="2"/>
      <path d="M4 52 L36 16" stroke="#fff" stroke-width="2"/>
    </svg>
    Better for the<br>enviroment
  </div>
  <div class="pillar-divider" style="left:391px"></div>
  <div class="pillar" style="left:401px">
    <svg width="54" height="54" viewBox="0 0 54 54" aria-hidden="true">
      <circle cx="27" cy="27" r="25" fill="none" stroke="#fff" stroke-width="2"/>
      <circle cx="27" cy="27" r="19" fill="none" stroke="#fff" stroke-width="2"/>
      <text x="27" y="36" text-anchor="middle" font-family="Poppins, sans-serif" font-weight="500" font-size="26" fill="#fff">$</text>
    </svg>
    Better for<br>your bottom line
  </div>

  <div class="abs closing">Powerful cleaning solutions.<br>Proven performance.<br><span class="accent">Real savings.</span></div>
</div>
</body>
</html>
```